Letterhead design for Sleep Consulting Business

I'm looking for a new letterhead (heading/footer) design for my Sleep Consulting Business, I work with families to help their children improve their sleep.

The heading/footer will used in Microsoft Word Only-to be used for all of my documents such as writing Sleep Plans. I need to utilize as much working space in the document as possible. This will NOT be printed out on paper- it will only be used for heading/footer on microsoft word, then emailed to clients, who may print it at home.

My brand colors:
Dark Blue Hex: 1F2A42
Lighter Blueish Hex: 90BEC9
You're welcome to check out my website for inspiration- it is freshly created with other colors as well, and I love the outcome. www.quietharborsleep.example

Target Market(s)

Tired parents

Font styles to use
Script
Other font styles liked:
• Great Vibe, Lato or Just Another Hand are all used currently for my brand. Open to other options.

Requirements
Must have
• The letterhead (heading/footer) MUST be kept narrow (height-wise), so I have plenty of space on my document, while including important information.

It should look professional on screen, and when printed.

Must include my business name OR logo (Quiet Harbor Sleep Consulting), and my email address. Tessa@quietharborsleep.example

Website is optional, not required, just if you need to fill in a spot: www.quietharborsleep.example

```html
<!DOCTYPE html>
<html lang="en">
<head>
<meta charset="utf-8">
<title>Quiet Harbor Sleep Consulting – Letterhead</title>
<link href="https://fonts.googleapis.com/css2?family=Montserrat:wght@500&family=Mulish:wght@400&family=Tinos&display=swap" rel="stylesheet">
<style>
  :root {
    --navy: #1F2A42;
    --sky: #90BEC9;
    --paper: #ffffff;
    --backdrop: #bbbbbb;
    --ink: #5f6063;
    --ink-soft: #6b6c70;
  }
  * { margin: 0; padding: 0; box-sizing: border-box; }
  html, body { width: 1200px; height: 1200px; overflow: hidden; background: var(--backdrop); }
  .letterhead {
    position: absolute; left: 183px; top: 61px;
    width: 834px; height: 1078px;
    background: var(--paper);
    overflow: hidden;
  }
  .header-band, .footer-band { position: absolute; left: 0; width: 834px; display: block; }
  .header-band { top: 0; height: 88px; }
  .footer-band { bottom: 0; height: 80px; }
  .brand {
    position: absolute; left: 86px; top: 70px;
    display: flex; align-items: center; gap: 16px;
  }
  .brand-dot { width: 68px; height: 68px; border-radius: 50%; background: var(--sky); }
  .brand-name {
    font-family: "Montserrat", sans-serif; font-weight: 500;
    font-size: 22px; color: var(--navy); letter-spacing: 0.3px;
  }
  .letter-body {
    position: absolute; left: 86px; top: 275px; width: 661px;
    color: var(--ink);
  }
  .salutation { font-family: "Montserrat", sans-serif; font-weight: 500; font-size: 15px; margin-bottom: 33px; }
  .paragraph {
    font-family: "Mulish", sans-serif; font-size: 12.4px; line-height: 20.8px;
    text-align: justify; margin-bottom: 22px;
  }
  .sender { margin-top: 14px; }
  .sender-name { font-family: "Montserrat", sans-serif; font-weight: 500; font-size: 16.5px; color: var(--ink); line-height: 1.1; }
  .sender-role { font-family: "Mulish", sans-serif; font-size: 11px; color: var(--ink-soft); }
  .signature {
    position: absolute; left: 86px; top: 798px; width: 192px; height: 64px;
    background: linear-gradient(90deg, #eef0f3, #f6f7f9);
  }
  .contact-line {
    position: absolute; left: 86px; top: 990px; width: 661px;
    display: flex; align-items: center; justify-content: space-between;
    font-family: "Tinos", serif; font-size: 20px; color: var(--navy);
  }
  .contact-item { display: flex; align-items: center; gap: 8px; }
  .contact-icon { width: 17px; height: 17px; }
</style>
</head>
<body>
<main class="letterhead">
  <svg class="header-band" viewBox="0 0 1042 110" preserveAspectRatio="none" aria-hidden="true">
    <path d="M0 0 H1042 V112 Q520 -60 0 80 Z" fill="var(--navy)"/>
    <path d="M0 72 Q500 -22 1042 100" fill="none" stroke="#ffffff" stroke-width="4"/>
    <path d="M0 62 Q460 -10 880 62 Q460 12 0 86 Z" fill="var(--sky)"/>
  </svg>

  <div class="brand">
    <span class="brand-dot"></span>
    <span class="brand-name">Quiet Harbor Sleep Consulting</span>
  </div>

  <section class="letter-body">
    <p class="salutation">Dear sir/Madam,</p>
    <p class="paragraph">Lorem Ipsum is simply dummy text of the printing and typesetting industry. Lorem Ipsum has been the industry's standard dummy text ever since the 1500s, when an unknown printer took a galley of type and scrambled it to make a type specimen book. It has survived not only five centuries, but also the leap into electronic typesetting, remaining essentially unchanged. It was popularised in the 1960s with the release of Typeset sheets</p>
    <p class="paragraph">Contrary to popular belief, Lorem Ipsum is not simply random text. It has roots in a piece of classical Latin literature from 45 BC, making it over 2000 years old. Walter Brennick, a Latin professor at Alder Ridge College in Vermont, looked up one of the more obscure Latin words, consectetur, from a Lorem Ipsum passage, and going through the cites of the word in classical literature, discovered the undoubtable source. Lorem Ipsum comes from sections 1.10.32 and 1.10.33 of "de Finibus Bonorum et Malorum" (The Extremes of Good and Evil) by Lucian Maro, written in 45 BC. This book is a treatise on the theory of ethics, very popular during the Renaissance. The first line of Lorem Ipsum, "Lorem ipsum dolor sit amet..", comes from a line in section 1.10.32. typesetting, remaining essentially unchanged. It was popularised in the 1960s with the release of Typeset sheets</p>
    <p class="paragraph">Lorem Ipsum is simply dummy text of the printing and typesetting industry. Lorem Ipsum has been the industry's standard dummy text ever since the 1500s, when an unknown printer took a galley of type and scrambled it to make a type specimen book. It has survived not only five centuries, but also the leap into electronic typesetting, remaining essentially unchanged. It was popularised in the 1960s with the release of Typeset sheets</p>
    <div class="sender">
      <p class="sender-name">Daniel R. Moss, Esq.</p>
      <p class="sender-role">Managing Attorney</p>
    </div>
  </section>

  <div class="signature" role="img" aria-label="Handwritten signature of the sender"></div>

  <div class="contact-line">
    <span class="contact-item">
      <svg class="contact-icon" viewBox="0 0 20 20" aria-hidden="true"><rect x="2" y="4.5" width="16" height="11" rx="1" fill="none" stroke="var(--navy)" stroke-width="1.8"/><path d="M2.5 5 L10 11 L17.5 5" fill="none" stroke="var(--navy)" stroke-width="1.8"/></svg>
      Tessa@quietharborsleep.example
    </span>
    <span class="contact-item">
      <svg class="contact-icon" viewBox="0 0 20 20" aria-hidden="true"><g fill="none" stroke="var(--navy)" stroke-width="1.4"><circle cx="10" cy="10" r="8"/><ellipse cx="10" cy="10" rx="3.6" ry="8"/><path d="M2 10 H18 M3.5 5.8 H16.5 M3.5 14.2 H16.5"/></g></svg>
      www.quietharborsleep.example
    </span>
  </div>

  <svg class="footer-band" viewBox="0 0 1042 100" preserveAspectRatio="none" aria-hidden="true">
    <path d="M0 8 Q560 128 1042 40 V100 H0 Z" fill="var(--navy)"/>
    <path d="M160 40 Q600 98 1042 26 V42 Q600 110 160 40 Z" fill="var(--sky)"/>
    <path d="M150 46 Q600 118 1042 48" fill="none" stroke="#ffffff" stroke-width="4"/>
  </svg>
</main>
</body>
</html>
```